Valundra - Plant extraction for human use

Valundra is a plant extraction based on long pepper containing a high concentration of piperlongumine. Piperlongumine has mainly anti-cancer properties, shown in many animal studies (200). It has as well shown to inhibit dementia and bone inflammation (in animal studies). We are the first to offer this extract for the European market. Because the product will be sold under a ‘plant extraction’ legislation, we cannot make any claims about the medical properties of the extract. I need a design for the packaging (blister pack) in a category for life enhancing medicine with no connotation of cancer for the European market in a first phase. We target people from 35-75 years old. For the younger group of people, we would propose (without saying) to use our product for chemoprevention against cancer. For those patients which have been diagnosed with cancer, we would propose to use it in conjunction with chemo-radio or immunotherapy (without saying).
Target Market(s)
Europe
Look and feel

```html
<!DOCTYPE html>
<html lang="en">
<head>
<meta charset="utf-8">
<title>Piperlongumine — Packaging</title>
<link href="https://fonts.googleapis.com/css2?family=Josefin+Sans:ital,wght@0,700;1,700&family=Quicksand:wght@500&family=Montserrat:wght@300&display=swap" rel="stylesheet">
<style>
  :root {
    --brand-blue: #3277b5;
    --deep-blue: #1f5aa6;
    --paper: #fafafa;
    --band: #ffffff;
    --ink: #0d0d0d;
    --stage: #e9eae6;
    --badge-green: #a6d48a;
  }
  html, body {
    margin: 0;
    width: 1200px;
    height: 1200px;
    overflow: hidden;
    background: var(--stage);
  }
  .package {
    position: absolute;
    left: 100px;
    top: 260px;
    width: 1000px;
  }
  .lid {
    height: 180px;
    background: var(--brand-blue);
    display: flex;
    align-items: center;
    justify-content: center;
  }
  .lid-name {
    font-family: "Josefin Sans", sans-serif;
    font-style: italic;
    font-weight: 700;
    font-size: 40px;
    letter-spacing: 3px;
    color: #ffffff;
  }
  .front {
    position: relative;
    height: 500px;
    background: var(--paper);
    overflow: hidden;
  }
  .front-band {
    position: absolute;
    left: 0;
    right: 0;
    top: 170px;
    height: 130px;
    background: var(--band);
  }
  .fragments {
    position: absolute;
    left: 0;
    top: 0;
    width: 290px;
    height: 500px;
  }
  .count {
    position: absolute;
    right: 90px;
    top: 70px;
    font-family: "Quicksand", sans-serif;
    font-weight: 500;
    font-size: 44px;
    color: var(--deep-blue);
    margin: 0;
  }
  .product-name {
    position: absolute;
    left: 150px;
    top: 200px;
    margin: 0;
    font-family: "Josefin Sans", sans-serif;
    font-weight: 700;
    font-size: 72px;
    letter-spacing: 3px;
    color: var(--ink);
  }
  .descriptor {
    position: absolute;
    left: 420px;
    top: 325px;
    margin: 0;
    font-family: "Montserrat", sans-serif;
    font-weight: 300;
    font-size: 28px;
    color: var(--ink);
  }
  .seal {
    position: absolute;
    right: 70px;
    bottom: 30px;
  }
</style>
</head>
<body>
  <main class="package">
    <section class="lid">
      <span class="lid-name">PIPERLONGUMINE</span>
    </section>
    <section class="front">
      <div class="front-band"></div>
      <svg class="fragments" role="img" aria-label="Shattered blue square fragments decoration" viewBox="0 0 290 500">
        <defs>
          <linearGradient id="frag" x1="0" y1="0" x2="0" y2="1">
            <stop offset="0" stop-color="#3277b5" stop-opacity="0.15"/>
            <stop offset="0.45" stop-color="#3277b5" stop-opacity="0.55"/>
            <stop offset="1" stop-color="#3277b5"/>
          </linearGradient>
        </defs>
        <rect width="290" height="500" fill="url(#frag)"/>
      </svg>
      <p class="count">36 tablets</p>
      <h1 class="product-name">PIPERLONGUMINE</h1>
      <p class="descriptor">Piper longum extract</p>
      <svg class="seal" width="120" height="120" viewBox="0 0 120 120" aria-hidden="true">
        <circle cx="60" cy="60" r="54" fill="none" stroke="var(--badge-green)" stroke-width="4"/>
      </svg>
    </section>
  </main>
</body>
</html>
```